"Tidelark Ministry" needs a logo design that represents a Christian family boating ministry

Mission Statement:
“Providing compassion, care and opportunities to create memories for marginalized groups of society through ocean therapy.”
Bible verse:
Colossians 3:12 – “Therefore, as God’s chosen people, holy and dearly loved, clothe yourselves with compassion, kindness, humility, gentleness and patience.”
Target Market(s)
HOMELESS (who have gone through shelters and are on the road to recovery)
CHURCH GROUPS
INJURED MILITARY VETERANS
YOUTH AT RISK (orphans, human trafficking survivors)
SICKLY (hospitalized who can get out once in a while)
CAREGIVERS (single moms, military spouses caring for injured vets, families of those in prison)
ELDERLY (retirement centers)
SMALL BUSINESS STAFF OUTINGS
SPECIAL EVENTS
Industry/Entity Type
Ministry
Contact Information for Business Card
Captain Glen Marbury @ 555-014-2931
Priscilla Marbury @ 555-018-6457
info@tidelarkministry-example.com
www.tidelarkministry-example.com (not active yet but hopefully, soon)
Requirements
Must have
- Catch-phrase words maybe for back of business card:
- "Tidelark --- Kindness --- Sharing days on the waves"
Nice to have
- Added 2 photo files just for visuals:
- 1 photo is of our boat.
- Other photo is our daughter's artwork on a cooler she made (for father's day gift)...might be nice and fun to incorporate daughter's artwork/inspiration into logo...but not sure if it looks to busy

```html
<!DOCTYPE html>
<html lang="en">
<head>
<meta charset="utf-8">
<title>Tidelark Ministry – Business Card</title>
<link rel="stylesheet" href="https://fonts.googleapis.com/css2?family=Open+Sans:wght@400;600&family=Kalam:wght@400&display=swap">
<style>
  :root {
    --backdrop: #2e2e2e;
    --card: #f1f1f1;
    --ink: #1f1f1f;
    --sea-blue: #3e8bbd;
    --sun-gold: #e3a52a;
    --ghost: #dcdcdc;
  }
  * { margin: 0; padding: 0; box-sizing: border-box; }
  html, body { width: 1200px; height: 600px; overflow: hidden; }
  body {
    background: var(--backdrop);
    font-family: "Open Sans", Arial, sans-serif;
    position: relative;
  }
  .card {
    position: absolute;
    top: 164px;
    width: 468px;
    height: 272px;
    background: var(--card);
    border-radius: 16px;
    overflow: hidden;
  }
  .card--front { left: 122px; }
  .card--back { left: 612px; }

  /* Front: contacts */
  .contact {
    position: absolute;
    top: 18px;
    padding: 0 10px;
    line-height: 1.25;
  }
  .contact--left { left: 18px; border-left: 10px solid var(--sea-blue); }
  .contact--right { right: 18px; border-right: 10px solid var(--sea-blue); text-align: right; }
  .contact__name { font-size: 15px; color: var(--ink); }
  .contact__phone { font-size: 15px; color: var(--sea-blue); }

  .ghost-circle {
    position: absolute;
    left: 0;
    top: 74px;
    width: 250px;
    height: 250px;
    border-radius: 50%;
    background: var(--ghost);
    opacity: .55;
  }

  .links {
    position: absolute;
    left: 20px;
    bottom: 22px;
    list-style: none;
    font-size: 12px;
    color: var(--ink);
  }
  .links li { display: flex; align-items: center; gap: 9px; margin-top: 8px; }
  .links svg { width: 11px; height: 11px; }

  /* Wordmark */
  .wordmark { position: absolute; text-align: center; }
  .wordmark__sun {
    display: block;
    border-radius: 50%;
    background: var(--sun-gold);
    margin: 0 auto;
  }
  .wordmark__name { color: var(--ink); font-weight: 400; letter-spacing: -0.5px; line-height: 1; }
  .wordmark__sub { color: var(--sea-blue); text-transform: uppercase; }

  .wordmark--small { right: 20px; bottom: 22px; }
  .wordmark--small .wordmark__sun { width: 74px; height: 74px; margin-bottom: 8px; }
  .wordmark--small .wordmark__name { font-size: 34px; }
  .wordmark--small .wordmark__sub { font-size: 10px; letter-spacing: 4px; margin-top: 2px; }

  .wordmark--large { left: 0; right: 0; top: 28px; }
  .wordmark--large .wordmark__sun { width: 88px; height: 88px; margin-bottom: 10px; }
  .wordmark--large .wordmark__name { font-size: 40px; }
  .wordmark--large .wordmark__sub { font-size: 12px; letter-spacing: 5px; margin-top: 3px; }

  .tagline {
    position: absolute;
    left: 0; right: 0;
    top: 192px;
    text-align: center;
    font-family: "Kalam", cursive;
    font-size: 15px;
    color: var(--sea-blue);
  }
  .waves { position: absolute; left: 0; bottom: 0; width: 468px; height: 92px; }
</style>
</head>
<body>
  <section class="card card--front" aria-label="Business card front">
    <div class="ghost-circle" aria-hidden="true"></div>

    <div class="contact contact--left">
      <p class="contact__name">Captain Glen Marbury</p>
      <p class="contact__phone">@ 555-014-2931</p>
    </div>
    <div class="contact contact--right">
      <p class="contact__name">Priscilla Marbury</p>
      <p class="contact__phone">@ 555-018-6457</p>
    </div>

    <ul class="links">
      <li>
        <svg viewBox="0 0 12 12" aria-hidden="true"><rect x="0.5" y="2" width="11" height="8" fill="none" stroke="#3e8bbd"/><path d="M0.5 2 L6 7 L11.5 2" fill="none" stroke="#3e8bbd"/></svg>
        info@tidelarkministry-example.com
      </li>
      <li>
        <svg viewBox="0 0 12 12" aria-hidden="true"><circle cx="6" cy="6" r="5.3" fill="none" stroke="#3e8bbd"/><ellipse cx="6" cy="6" rx="2.3" ry="5.3" fill="none" stroke="#3e8bbd"/><path d="M0.7 6 H11.3" stroke="#3e8bbd"/></svg>
        www.tidelarkministry-example.com
      </li>
    </ul>

    <div class="wordmark wordmark--small">
      <span class="wordmark__sun" aria-hidden="true"></span>
      <p class="wordmark__name">Tidelark</p>
      <p class="wordmark__sub">Kindness</p>
    </div>
  </section>

  <section class="card card--back" aria-label="Business card back">
    <div class="wordmark wordmark--large">
      <span class="wordmark__sun" aria-hidden="true"></span>
      <p class="wordmark__name">Tidelark</p>
      <p class="wordmark__sub">Kindness</p>
    </div>
    <p class="tagline">Sharing days on the waves</p>

    <svg class="waves" viewBox="0 0 468 92" preserveAspectRatio="none" aria-hidden="true">
      <path d="M0 0 C60 10 150 46 240 40 C320 34 380 26 400 26 C330 40 240 62 150 60 C90 58 40 48 0 52 Z" fill="var(--sun-gold)"/>
      <path d="M0 62 C60 54 120 70 200 70 C290 70 380 28 468 36 L468 92 L0 92 Z" fill="var(--sea-blue)"/>
    </svg>
  </section>
</body>
</html>
```